Ridgewell Hauling Business Cards & Stantionery
Dump Truck Services
Ridgewell Hauling Business Cards & Stantionery -
Creative Brief
Professional
Osvaldo Mireles, Jr.
Owner
4158 Fenwick Rd. Pearland, TX 77590
osvaldo@ridgewellhauling-demo.com
www.ridgewellhauling-demo.com

```html
<!DOCTYPE html>
<html lang="en">
<head>
<meta charset="utf-8">
<title>Ridgewell Hauling Stationery</title>
<link href="https://fonts.googleapis.com/css2?family=Roboto:wght@400;500;700&display=swap" rel="stylesheet">
<style>
:root{
  --red:#c8102e;
  --red-dark:#960b20;
  --navy:#1f2f73;
  --paper:#ffffff;
  --paper-shade:#f1f1f1;
  --ink:#333333;
  --muted:#8a8a8a;
  --bg:#e8e5e1;
}
*{margin:0;padding:0;box-sizing:border-box}
html,body{width:1200px;height:490px;overflow:hidden}
body{background:var(--bg);font-family:"Roboto",Arial,sans-serif;color:var(--ink);position:relative}
.piece{position:absolute;background:var(--paper);box-shadow:0 2px 6px rgba(0,0,0,.18);overflow:hidden}
.wave{position:absolute;left:0;bottom:0;width:100%}
.brand{display:flex;align-items:center;gap:5px;font-weight:700;color:var(--red);text-transform:uppercase;line-height:1.05;letter-spacing:.3px}
.brand .dot{border-radius:50%;background:var(--red);flex:none}
.brand span{display:block}

/* business cards */
.card{width:168px;height:104px;left:96px;border-radius:5px}
.card-front{top:96px}
.card-front .brand{position:absolute;left:10px;top:14px;font-size:8px}
.card-front .brand .dot{width:14px;height:14px}
.card-front .person{position:absolute;right:12px;top:18px;text-align:right;font-size:6px;line-height:1.4}
.card-front .person strong{font-size:7px;color:var(--ink)}
.card-info{top:222px;background:linear-gradient(180deg,#ffffff,#ececec)}
.faint-circle{position:absolute;border-radius:50%}
.card-info .faint-circle{width:78px;height:78px;left:44px;top:12px;background:rgba(200,16,46,.08)}
.card-info .contact{position:absolute;left:12px;bottom:14px;font-size:5.5px;line-height:1.5;color:var(--muted)}
.card-back{top:350px;background:linear-gradient(160deg,var(--red),var(--red-dark))}
.card-back .faint-circle{width:96px;height:96px;right:-10px;top:4px;background:rgba(255,255,255,.1)}
.card-back .web{position:absolute;left:12px;bottom:12px;font-size:5.5px;color:#fff}

/* sheets */
.sheet{width:232px;height:372px;top:84px}
.letterhead{left:283px}
.fax{left:552px}
.sheet .brand{position:absolute;left:16px;top:22px;font-size:11px}
.sheet .brand .dot{width:18px;height:18px}
.sheet .addr{position:absolute;right:16px;top:22px;font-size:5px;line-height:1.55;color:var(--muted)}
.letterhead .faint-circle{width:120px;height:120px;left:-20px;top:120px;background:rgba(200,16,46,.06)}
.fax-title{position:absolute;right:16px;top:64px;font-size:9px;font-weight:700;color:var(--red)}
.fax-fields{position:absolute;left:16px;right:16px;top:80px;display:grid;grid-template-columns:1fr 1fr;column-gap:12px;row-gap:6px;font-size:5.5px}
.fax-fields div{border-bottom:.6px solid #bbb;padding-bottom:2px}
.fax-checks{position:absolute;left:16px;right:16px;top:128px;display:flex;justify-content:space-between;font-size:5px}
.fax-checks span::before{content:"";display:inline-block;width:5px;height:5px;border:.6px solid #888;margin-right:2px;vertical-align:-1px}
.fax .faint-circle{width:120px;height:120px;left:-20px;top:150px;background:rgba(200,16,46,.06)}

/* envelopes */
.envelope{width:250px;height:112px;left:818px}
.env-back{top:146px}
.env-back .flap{position:absolute;left:0;top:0;width:100%;height:100%}
.env-back .seal{position:absolute;left:50%;top:44px;transform:translateX(-50%);width:18px;height:18px;border-radius:50%;background:#fff}
.env-front{top:286px}
.env-front .brand{position:absolute;left:14px;top:14px;font-size:8px}
.env-front .brand .dot{width:14px;height:14px}
.env-front .ret{position:absolute;left:14px;top:42px;font-size:5px;line-height:1.5;color:var(--muted)}
.env-front .band{position:absolute;right:0;top:0;width:60px;height:100%}
</style>
</head>
<body>

<!-- business card front -->
<div class="piece card card-front">
  <div class="brand"><i class="dot"></i><div><span>Ridgewell</span><span>Hauling</span></div></div>
  <div class="person"><strong>Osvaldo Mireles, Jr.</strong><br>Owner<br>(281) 555-0147</div>
  <svg class="wave" viewBox="0 0 168 40" height="40" preserveAspectRatio="none">
    <path d="M0 22 Q84 6 168 18 L168 40 L0 40Z" fill="var(--red)"/>
    <path d="M0 18 Q84 2 168 14" stroke="var(--navy)" stroke-width="1" fill="none"/>
  </svg>
</div>

<!-- business card info side -->
<div class="piece card card-info">
  <div class="faint-circle"></div>
  <div class="contact">4158 Fenwick Rd. Pearland, TX 77590<br>osvaldo@ridgewellhauling-demo.com</div>
</div>

<!-- business card back -->
<div class="piece card card-back">
  <div class="faint-circle"></div>
  <div class="web">www.ridgewellhauling-demo.com</div>
</div>

<!-- letterhead -->
<div class="piece sheet letterhead">
  <div class="brand"><i class="dot"></i><div><span>Ridgewell</span><span>Hauling</span></div></div>
  <div class="addr">4158 Fenwick Rd.<br>Pearland, TX 77590<br>Ph (281) 555-0147<br>www.ridgewellhauling-demo.com</div>
  <div class="faint-circle"></div>
  <svg class="wave" viewBox="0 0 232 50" height="50" preserveAspectRatio="none">
    <path d="M0 26 Q116 4 232 22 L232 50 L0 50Z" fill="var(--red)"/>
    <path d="M0 20 Q116 -2 232 16" stroke="var(--navy)" stroke-width="1.2" fill="none"/>
  </svg>
</div>

<!-- fax sheet -->
<div class="piece sheet fax">
  <div class="brand"><i class="dot"></i><div><span>Ridgewell</span><span>Hauling</span></div></div>
  <div class="addr">4158 Fenwick Rd.<br>Pearland, TX 77590<br>Ph (281) 555-0147<br>www.ridgewellhauling-demo.com</div>
  <div class="fax-title">Fax Sheet</div>
  <div class="fax-fields">
    <div>To:</div><div>From:</div>
    <div>Fax:</div><div>Date:</div>
    <div>Re:</div><div>Pages:</div>
  </div>
  <div class="fax-checks"><span>Urgent</span><span>For Review</span><span>Please Comment</span><span>Please Reply</span></div>
  <div class="faint-circle"></div>
  <svg class="wave" viewBox="0 0 232 50" height="50" preserveAspectRatio="none">
    <path d="M0 26 Q116 4 232 22 L232 50 L0 50Z" fill="var(--red)"/>
    <path d="M0 20 Q116 -2 232 16" stroke="var(--navy)" stroke-width="1.2" fill="none"/>
  </svg>
</div>

<!-- envelope back -->
<div class="piece envelope env-back">
  <svg class="flap" viewBox="0 0 250 112" preserveAspectRatio="none">
    <path d="M0 0 L250 0 L250 14 Q125 78 0 14Z" fill="var(--red)"/>
    <path d="M0 14 Q125 84 250 14" stroke="var(--navy)" stroke-width="1" fill="none"/>
    <path d="M0 112 L110 62 M250 112 L140 62" stroke="#dddddd" stroke-width="1"/>
  </svg>
  <div class="seal"></div>
</div>

<!-- envelope front -->
<div class="piece envelope env-front">
  <div class="brand"><i class="dot"></i><div><span>Ridgewell</span><span>Hauling</span></div></div>
  <div class="ret">4158 Fenwick Rd.<br>Pearland, TX 77590</div>
  <svg class="band" viewBox="0 0 60 112" preserveAspectRatio="none">
    <path d="M60 0 L60 112 L40 112 Q10 56 40 0Z" fill="var(--red)"/>
    <path d="M36 0 Q6 56 36 112" stroke="var(--navy)" stroke-width="1" fill="none"/>
  </svg>
</div>

</body>
</html>
```